Book cover for middle grade children's book

I need a book cover design for the first book in my middle grade series aimed at girls ages 9-12.

PLEASE SEE MY ATTACHED EXAMPLES.

Title: Pim Dorsey: Cousin Mabel's Payback

Design Brief:
Front: I want it to look like a composition book. The background should be a pink plaid design. There should be a white square in the center like a composition book. On top of the square in purple letters should be the name Pim. Underneath the square should be the name Dorsey. Pim Dorsey should be in a fun girly font that's readible on thumbnail. The sub title should go on the white square where a kid would write their name. It should say Cousin Mabel's Payback in a girl's pink handwriting. At the bottom underneath Dorsey should be my name: Rhonda Louise Barlow

On the left side there should be a dark pink or purple (whichever looks best with the pattern) strip like composition books have.

Spine: Pim Dorsey: Cousin Mabel's Payback (Pim Dorsey #1) Barlow

On the back: I'd like the back to be hot pink with white font.

Thirteen-year-old Pim Dorsey has a lot on her plate. Her biggest challenge is living with her Cousin Mabel. As much as Pim tries to please her aunt,, they always seem to butt heads. Sometimes Pim feels as if Cousin Mabel goes out of her way to make her life miserable.

Cousin Mabel enrolls Pim in a social group called the Golden Finches, a group that's supposed to teach young girls how to be proper ladies, however it turns out to be nothing more than a club for snobs. Pim wants out, but she's made a deal with Cousin Mabel. Will Pim take a stand against the Golden Finches or will their snobbery rub off on her?
IT'S VERY IMPORTANT THAT IT LOOKS LIKE A COMPOSITION BOOK SINCE THAT WILL BE THE BRAND FOR THE SERIES.

I need this cover to fit the mandates for ebook and pressnook. Place follow the correct measurements.

This book will be 160 pages on cream paper. 6x9

Target Market(s)

Girls ages 9 and up

Industry/Entity Type

Club

Requirements
Must have
• Readable professional looking font
Should not have
• A background pattern that too busy and clashes with the font

```html
<!DOCTYPE html>
<html lang="en">
<head>
<meta charset="utf-8">
<title>Pim Dorsey: Cousin Mabel's Payback – Back Cover</title>
<link rel="stylesheet" href="https://fonts.googleapis.com/css2?family=Schoolbell&family=Lato:wght@400&display=swap">
<style>
  :root {
    --plaid-light: #f48fb6;
    --plaid-mid: #ee6fa3;
    --plaid-deep: #e8488d;
    --strip-purple: #9b4a9e;
    --text-white: #ffffff;
  }
  html, body {
    margin: 0;
    padding: 0;
    width: 800px;
    height: 1200px;
    overflow: hidden;
    background: #ffffff;
  }
  .back-cover {
    position: relative;
    width: 800px;
    height: 1200px;
    overflow: hidden;
  }
  .plaid-field {
    position: absolute;
    left: 0;
    top: 0;
    width: 720px;
    height: 1200px;
    background: linear-gradient(160deg, var(--plaid-mid) 0%, var(--plaid-light) 45%, var(--plaid-mid) 75%, var(--plaid-deep) 100%);
  }
  .binding-strip {
    position: absolute;
    left: 720px;
    top: 0;
    width: 80px;
    height: 1200px;
    background: var(--strip-purple);
  }
  .blurb {
    position: absolute;
    left: 89px;
    top: 120px;
    width: 551px;
    color: var(--text-white);
  }
  .blurb-title {
    margin: 0 0 14px 4px;
    font-family: "Schoolbell", cursive;
    font-weight: 400;
    font-size: 54px;
    line-height: 1.1;
    letter-spacing: 1px;
    white-space: nowrap;
  }
  .blurb-text {
    margin: 0;
    font-family: "Lato", sans-serif;
    font-size: 28.5px;
    line-height: 42.2px;
    text-align: justify;
    text-align-last: center;
    hyphens: auto;
  }
</style>
</head>
<body>
  <main class="back-cover">
    <div class="plaid-field" role="img" aria-label="Pink plaid composition-book pattern in hot pink and light pink"></div>
    <div class="binding-strip"></div>
    <section class="blurb">
      <h1 class="blurb-title">Cousin Mabel's Payback</h1>
      <p class="blurb-text">Thirteen-year-old Pim Dorsey has a lot on her plate. Her biggest challenge is living with her Cousin Mabel. As much as Pim tries to please her aunt,, they always seem to butt heads. Sometimes Pim feels as if Cousin Mabel goes out of her way to make her life miserable. Cousin Mabel enrolls Pim in a social group called the Golden Finches, a group that's supposed to teach young girls how to be proper ladies, however it turns out to be nothing more than a club for snobs. Pim wants out, but she's made a deal with Cousin Mabel. Will Pim take a stand against the Golden Finches or will their snobbery rub off on her?</p>
    </section>
  </main>
</body>
</html>
```